Wine Label for a syrah wine hand crafted from walla walla valley, washington

design a wine label for the name of the brand: Lumaret. It is a wine hand crafted from Walla Walla Valley in Washington state. the label should be landscape in design, 95 mm wide by 85 mm tall. it should include the name of the brand, Lumaret, Walla Walla Valley, 2020 and Syrah. the brand is called lumaret with this in mind:

-lumaret Definition & Meaning |
1. : having (something) at the center. The solar system is helio lumaret, meaning that the sun is at its center. 2. : having (something) as a central interest, influence, subject, in the case of this wine label it is Syrah wine from Walla Walla Valley
this american vitculture area is known for wines which showcase the terrior of the area - this wine is specifically from the Rocks district where there are lots of rocks in the vineyard. think terrior, rocks, dirt, grapes that are hand crafted into a bottle of wine that will cost $125 each.

Target Market(s)

syrah lovers, Rhone valley wine lovers,

Industry/Entity Type

wine industry

Font styles to use
Sans Serif
Other font styles liked:
• freightbig in light, book and medium weights

Requirements
Must have
• the elements described in the project description, please use FreightBig font found on brivant site, light, book and medium weights
Nice to have
• a cool edgy design but elegant a the same time
Should not have
• stock pictures

```html
<!DOCTYPE html>
<html lang="en">
<head>
<meta charset="utf-8">
<title>Lumaret Syrah – Wine Label</title>
<link rel="stylesheet" href="https://fonts.googleapis.com/css2?family=Lato:wght@300&family=Playfair+Display:wght@400&family=Libre+Baskerville&display=swap">
<style>
  :root {
    --page: #ffffff;
    --label-ground: #4b3435;
    --copper: #f4a46a;
    --copper-ring: #8f654f;
    --band-tone: #5e4442;
    --ivory: #ffffff;
  }
  html, body {
    margin: 0;
    width: 881px;
    height: 1200px;
    overflow: hidden;
    background: var(--page);
  }
  .canvas {
    position: relative;
    width: 881px;
    height: 1200px;
  }
  .wine-label {
    position: absolute;
    left: 40px;
    top: 241px;
    width: 801px;
    height: 717px;
    display: block;
  }
  .label-ground { fill: var(--label-ground); }
  .band-rule { stroke: var(--copper); stroke-width: 2; }
  .band-pattern { fill: var(--band-tone); }
  .center-ring { fill: none; stroke: var(--copper-ring); stroke-width: 28; }
  .brand-name {
    font-family: "Lato", sans-serif;
    font-weight: 300;
    font-size: 100px;
    letter-spacing: 5px;
    fill: var(--copper);
  }
  .varietal {
    font-family: "Playfair Display", serif;
    font-size: 40px;
    letter-spacing: 19px;
    fill: var(--ivory);
  }
  .region {
    font-family: "Libre Baskerville", serif;
    font-size: 15px;
    letter-spacing: -0.6px;
    fill: var(--ivory);
  }
  .region-rule { stroke: var(--copper); stroke-width: 1.5; }
  .vintage {
    font-family: "Libre Baskerville", serif;
    font-size: 12px;
    letter-spacing: 5px;
    fill: var(--ivory);
  }
</style>
</head>
<body>
<main class="canvas">
  <svg class="wine-label" viewBox="0 0 801 717" xmlns="http://www.w3.org/2000/svg">
    <defs>
      <linearGradient id="terrain-glow" x1="0" y1="0" x2="0" y2="1">
        <stop offset="0" stop-color="#f4a46a" stop-opacity="0"/>
        <stop offset="1" stop-color="#f4a46a" stop-opacity="0.16"/>
      </linearGradient>
    </defs>

    <rect class="label-ground" x="0" y="0" width="801" height="717"/>

    <g class="top-band">
      <rect class="band-pattern" x="0" y="33" width="801" height="90" role="img" aria-label="Interlocking circle lattice pattern band"/>
      <line class="band-rule" x1="0" y1="32" x2="801" y2="32"/>
      <line class="band-rule" x1="0" y1="124" x2="801" y2="124"/>
    </g>

    <rect class="terrain-field" x="0" y="390" width="801" height="327" fill="url(#terrain-glow)" role="img" aria-label="Flowing copper line mesh evoking rolling vineyard terrain"/>

    <circle class="center-ring" cx="402" cy="358" r="184"/>

    <text class="brand-name" x="402" y="294" text-anchor="middle">LUMARET</text>
    <text class="varietal" x="410" y="376" text-anchor="middle">SYRAH</text>
    <text class="region" x="402" y="467" text-anchor="middle">WALLA WALLA VALLEY</text>
    <line class="region-rule" x1="306" y1="472" x2="498" y2="472"/>
    <text class="vintage" x="404" y="487" text-anchor="middle">2020</text>
  </svg>
</main>
</body>
</html>
```